Stylish Website Design for Harbourline Plunge Tanks

Harbourline Plunge Tanks will be building a new website in a Wordpress CMS.
The design will be stylish, clean with strong powerful images that represent their work. Users scrolling pages will have call to actions listed at various intervals that drives traffic through the website journey.
The objective of the website journey is to direct clients to the ‘Instant Quote’. This will take visitors through an 8 Step calculator.
1. Capture Customer Details (Email and Full Name).
2. Pool Size
3. Shell Colour
4. Exterior Colour
5. Decking Option
6. Access Options
7. Selections (choosing the sanitisation and pump)
8. Extras
The instant quote will be visually appealing and engaging. The next button for each step will capture the data and identify the step the customer aborts.
Here is a link to the current calculator OLD QUOTE: https://harbourlineplungetanks.com.au/quote
The current design has the following issues that need to be resolved with the new design, please do not replicate the current look and feel. We are seeking a complete redesign of the website.
1. No scrolling to go to the next tap.
2. Improve the image layout
3. Selections and Extras needs to be like an eCommerce site with images, access to descriptions, specifications etc.
4. The steps need to feel like a journey
5. Gathering the customer’s name and email must be captured at the beginning
The aim is to keep the design simple but stylish. The navigation should have a search bar and clearly display the phone number as a link not an image, so it can be clicked on to make a call from a mobile device.
Please note the current website does not have the current logo, only a temporary one. Please use this one, the logo may be redesigned. https://filevault.examplestore.net/external/9c41e7a2b8d05f36e1c7a94b0d2e58f3a61c7b94e02d8f5a3b6c1e97d40a8f2b
IMAGES: Here are some of the company’s professional images. https://filevault.examplestore.net/external/3e8a06d2f7b14c95a0d3e6f18b27c4a9d5e01f6b38a2c7d94e15b0f6a2c83d7e
There must be call to actions as you scroll the page.
• Contact Us Button
• Download Brochure (name may be changed)
o This will capture a customers name and email to send a brochure
• Join Our Team
• Live Chat (Floats bottom right)
• Order Now Button
Site Map
• Home page – via logo
• Design and Build - http://harbourlineplungetanks.com.au/learn-more
o Instant Quote
o Packages
There may be 3 packages
o The Process
o Financing
• About Us
o Choosing Us
o Locations
o Careers
• Blogs
o Events
o Legends
• Gallery
• Contact Us
Footer
• Social Media icons
o TikTok
o Instagram
o Facebook
o Youtube
o Twitter
• Privacy Policy (Content on the current site but improve layout)
• Specifications
• Site Map
• Images of Certifications (as shown on the current site)
• Company Contact Details (Address on Phone)
• Marketing News Sign Up
Target Market(s)
Business to Consumer, Renovations
Industry/Entity Type
Construction and Renovations
Number of Pages Required
5+ page
Requirements
Must have
- Read the description but home page design and calculator design.
Nice to have
- Included in the description.

```html
<!DOCTYPE html>
<html lang="en">
<head>
<meta charset="utf-8">
<title>Harbourline Plunge Tanks – Pool Size</title>
<link href="https://fonts.googleapis.com/css2?family=Oswald:wght@400;500&family=Open+Sans:wght@400;600&display=swap" rel="stylesheet">
<style>
:root{
  --orange:#F7941D;
  --orange-soft:#f9b66a;
  --peach:#FDE7CE;
  --ink:#1e1e1e;
  --muted:#8f8f8f;
  --light:#f5f5f5;
  --line:#e4e4e4;
  --white:#ffffff;
  --tank-blue:#2f7fe0;
  --tank-dark:#3a3d44;
}
*{box-sizing:border-box;margin:0;padding:0}
html,body{width:912px;height:1200px;overflow:hidden}
body{background:var(--peach);font-family:"Open Sans",sans-serif;color:var(--ink);position:relative}
.screen{position:absolute;top:248px;height:704px;background:var(--white);box-shadow:0 6px 22px rgba(0,0,0,.08);overflow:hidden}
.screen > *{position:absolute}
a{text-decoration:none;color:inherit}
.oswald{font-family:"Oswald",sans-serif}

/* shared pieces */
.topbar{left:0;right:0;top:0;background:var(--orange);color:var(--white);display:flex;align-items:center;justify-content:space-between}
.phone{display:flex;align-items:center;gap:3px;white-space:nowrap}
.social-squares{display:flex;gap:3px}
.social-squares span{display:block;background:rgba(255,255,255,.4)}
.header{left:0;right:0;background:var(--light);display:flex;align-items:center}
.logo{display:flex;align-items:center;gap:5px}
.logo-dot{border-radius:50%;background:var(--orange);flex:none}
.logo-name{font-family:"Oswald",sans-serif;font-weight:500;color:var(--orange);text-transform:uppercase;line-height:1.1}
.step-head{display:flex;justify-content:space-between;align-items:center;border-bottom:1px solid var(--line);font-family:"Oswald",sans-serif;text-transform:uppercase;white-space:nowrap}
.step-next{color:var(--orange)}
.photo-frame{border:1px solid var(--line);position:relative;background:var(--white)}
.tank-render{position:absolute;background:radial-gradient(ellipse at 55% 45%,#4d97ee 0%,#2a66c4 38%,#3a3d44 70%,#ffffff 100%)}
.arrow{position:absolute;top:50%;transform:translateY(-50%);color:var(--muted);line-height:1}
.thumbs{display:flex;justify-content:space-between}
.thumb{background:var(--light);display:flex;align-items:center;justify-content:center}
.thumb.active{background:var(--white);box-shadow:0 1px 6px rgba(0,0,0,.14)}
.thumb i{display:block;background:linear-gradient(90deg,#1c56b5,var(--tank-blue))}
.product-title{font-family:"Oswald",sans-serif;font-weight:500;line-height:1.15;white-space:nowrap}
.pid{color:var(--muted);text-transform:uppercase;white-space:nowrap}
.acc-head{display:flex;justify-content:space-between;align-items:center;white-space:nowrap}
.acc-open .acc-head{background:var(--orange);color:var(--white);font-weight:600}
.acc-row{background:var(--light)}
.chev{font-size:.9em}
.sizes{display:flex;align-items:center}
.size{background:var(--light);display:flex;flex-direction:column;align-items:center;justify-content:center;color:var(--orange)}
.size.active{background:var(--white);border:1px solid var(--orange-soft)}
.size b{font-family:"Oswald",sans-serif;font-weight:400;line-height:1.1}
.size small{color:var(--orange-soft)}
.subscribe{left:0;right:0;background:var(--light)}
.sub-title{font-family:"Oswald",sans-serif;font-weight:500;text-transform:uppercase;white-space:nowrap}
.sub-form{display:flex}
.sub-input{background:var(--white);border:1px solid var(--line);color:var(--muted);display:flex;align-items:center}
.sub-btn{background:var(--orange);color:var(--white);font-family:"Oswald",sans-serif;font-weight:500;text-transform:uppercase;display:flex;align-items:center;justify-content:center}
.footer{left:0;right:0;bottom:0;background:var(--orange);color:var(--white)}
.social-dots{display:flex;justify-content:center}
.social-dots span{display:block;border-radius:50%;background:var(--white)}
.foot-links{text-align:center;text-transform:uppercase;letter-spacing:.08em;white-space:nowrap}
.btn-quote{background:var(--orange);color:var(--white);font-family:"Oswald",sans-serif;font-weight:500;text-transform:uppercase;display:flex;align-items:center;justify-content:center}

/* desktop */
.desktop{left:26px;width:680px}
.desktop .topbar{height:19px;padding:0 91px 0 92px;font-size:5.8px}
.desktop .social-squares span{width:9px;height:9px}
.desktop .header{top:19px;height:64px;padding:0 91px 0 92px}
.desktop .logo{width:148px}
.desktop .logo-dot{width:10px;height:10px}
.desktop .logo-name{font-size:10px}
.desktop .nav{display:flex;gap:13px;font-family:"Oswald",sans-serif;font-weight:500;font-size:7.6px;text-transform:uppercase;white-space:nowrap}
.desktop .btn-quote{margin-left:auto;width:62px;height:22px;font-size:6px}
.desktop .step-head{left:92px;width:497px;top:126px;height:28px;font-size:8px}
.desktop .step-next{font-size:6px}
.desktop .gallery{left:93px;top:172px;width:241px}
.desktop .photo-frame{height:218px}
.desktop .tank-render{left:30px;right:30px;top:22px;bottom:22px}
.desktop .arrow{font-size:12px}
.desktop .arrow.prev{left:10px}.desktop .arrow.next{right:10px}
.desktop .thumbs{margin-top:8px}
.desktop .thumb{width:42px;height:42px}
.desktop .thumb i{width:38px;height:12px}
.desktop .thumb.active i{width:24px;height:16px}
.desktop .details{left:388px;top:172px;width:201px}
.desktop .product-title{font-size:18.5px}
.desktop .pid{font-size:5.6px;margin-top:3px}
.desktop .acc-open{margin-top:13px}
.desktop .acc-head{height:20px;padding:0 8px;font-size:5.8px}
.desktop .acc-text{font-size:5.4px;line-height:12px;padding:6px 8px 9px}
.desktop .acc-row{margin-top:5px}
.desktop .sizes{margin-top:13px}
.desktop .sizes label{font-size:5.8px;width:64px}
.desktop .size{width:65px;height:65px;margin-left:5px}
.desktop .size b{font-size:15px}
.desktop .size small{font-size:6.2px}
.desktop .subscribe{top:491px;height:129px;display:flex;align-items:center;justify-content:space-between;padding:0 91px 0 92px}
.desktop .sub-title{display:flex;align-items:center;gap:7px;font-size:17px}
.desktop .sub-input{width:127px;height:28px;padding:0 10px;font-size:5.6px}
.desktop .sub-btn{width:71px;height:28px;font-size:6px}
.desktop .footer{height:84px}
.desktop .social-dots{gap:9px;margin:24px 92px 0;padding-bottom:10px;border-bottom:1px solid rgba(255,255,255,.35)}
.desktop .social-dots span{width:10px;height:10px}
.desktop .foot-links{font-size:5.6px;margin-top:12px}

/* mobile */
.mobile{left:735px;width:151px}
.mobile .topbar{height:15px;justify-content:center;font-size:4.2px}
.mobile .header{top:15px;height:38px;padding:0 10px;justify-content:space-between}
.mobile .logo-dot{width:7px;height:7px}
.mobile .logo-name{font-size:6.2px}
.mobile .burger{display:flex;flex-direction:column;gap:1.5px}
.mobile .burger span{display:block;width:8px;height:1px;background:var(--orange)}
.mobile .step-head{left:10px;width:131px;top:82px;height:16px;font-size:4.8px}
.mobile .step-next{font-size:3.8px}
.mobile .gallery{left:10px;top:111px;width:131px}
.mobile .photo-frame{height:118px}
.mobile .tank-render{left:14px;right:14px;top:12px;bottom:12px}
.mobile .arrow{font-size:7px}
.mobile .arrow.prev{left:4px}.mobile .arrow.next{right:4px}
.mobile .thumbs{margin-top:7px}
.mobile .thumb{width:22px;height:17px}
.mobile .thumb i{width:20px;height:6px}
.mobile .thumb.active i{width:12px;height:9px}
.mobile .details{left:10px;top:276px;width:131px}
.mobile .product-title{font-size:9.6px}
.mobile .pid{font-size:3.8px;margin-top:2px}
.mobile .acc-open{margin-top:9px}
.mobile .acc-head{height:16px;padding:0 5px;font-size:4.2px}
.mobile .acc-text{font-size:3.7px;line-height:9.4px;padding:4px 5px 6px}
.mobile .acc-row{margin-top:4px}
.mobile .acc-row .acc-head{height:15px}
.mobile .sizes{margin-top:6px}
.mobile .sizes label{font-size:3.8px;width:50px}
.mobile .size{width:40px;height:40px;margin-left:2px}
.mobile .size b{font-size:9px}
.mobile .size small{font-size:3.5px}
.mobile .subscribe{top:502px;height:140px;display:flex;flex-direction:column;align-items:center;padding-top:34px}
.mobile .sub-title{font-size:9.4px;text-align:center;line-height:1.3;margin-top:5px}
.mobile .sub-form{margin-top:8px}
.mobile .sub-input{width:76px;height:20px;padding:0 7px;font-size:3.6px}
.mobile .sub-btn{width:55px;height:20px;font-size:4px}
.mobile .footer{height:62px}
.mobile .social-dots{gap:6px;margin-top:15px}
.mobile .social-dots span{width:7px;height:7px}
.mobile .foot-links{font-size:3.6px;margin-top:14px}
</style>
</head>
<body>

<div class="screen desktop">
  <div class="topbar">
    <a class="phone" href="tel:+61755500148"><svg width="6" height="6" viewBox="0 0 24 24"><path fill="#fff" d="M6.6 10.8a15 15 0 0 0 6.6 6.6l2.2-2.2a1 1 0 0 1 1-.25 11.4 11.4 0 0 0 3.6.57 1 1 0 0 1 1 1V20a1 1 0 0 1-1 1A17 17 0 0 1 3 4a1 1 0 0 1 1-1h3.5a1 1 0 0 1 1 1c0 1.25.2 2.45.57 3.6a1 1 0 0 1-.25 1z"/></svg>61 7 5550 0148</a>
    <div class="social-squares" aria-label="Social links"><span></span><span></span><span></span></div>
  </div>
  <header class="header">
    <a class="logo" href="#"><span class="logo-dot"></span><span class="logo-name">Harbourline<br>Plunge Tanks</span></a>
    <nav class="nav"><a href="#">Design and Build</a><a href="#">About Us</a><a href="#">Blog</a><a href="#">Gallery</a><a href="#">Contact Us</a></nav>
    <a class="btn-quote" href="#">Instant Quote</a>
  </header>
  <div class="step-head"><span>01 - Pool Size</span><a class="step-next" href="#">Next Option - Interval Colors &#8594;</a></div>
  <div class="gallery">
    <div class="photo-frame">
      <div class="tank-render" role="img" aria-label="Product render of a container plunge tank with dark cladding and blue interior"></div>
      <span class="arrow prev">&#8592;</span><span class="arrow next">&#8594;</span>
    </div>
    <div class="thumbs">
      <div class="thumb"><i role="img" aria-label="Tank view"></i></div>
      <div class="thumb active"><i role="img" aria-label="Tank view"></i></div>
      <div class="thumb"><i role="img" aria-label="Tank view"></i></div>
      <div class="thumb"><i role="img" aria-label="Tank view"></i></div>
      <div class="thumb"><i role="img" aria-label="Tank view"></i></div>
    </div>
  </div>
  <div class="details">
    <h1 class="product-title">Harbourline Plunge Tank</h1>
    <p class="pid">Product ID: 123 Text Filler</p>
    <div class="acc-open">
      <div class="acc-head"><span>Description</span><span class="chev">&#8963;</span></div>
      <p class="acc-text">Lorem Ipsum is simply dummy text of the printing and typesetting industry. Lorem Ipsum has been the industry's standard dummy text ever since the 1500s, when an unknown printer took a galley of type and scrambled it to make a type specimen book.</p>
    </div>
    <div class="acc-row"><div class="acc-head"><span>Features</span><span class="chev">&#8964;</span></div></div>
    <div class="acc-row"><div class="acc-head"><span>Specifications</span><span class="chev">&#8964;</span></div></div>
    <div class="acc-row"><div class="acc-head"><span>Text Filler</span><span class="chev">&#8964;</span></div></div>
    <div class="sizes">
      <label>Select a Pool Size:</label>
      <div class="size active"><b>6m</b><small>6m x 2.4m</small></div>
      <div class="size"><b>12m</b><small>12m x 2.4m</small></div>
    </div>
  </div>
  <section class="subscribe">
    <h2 class="sub-title"><svg width="16" height="12" viewBox="0 0 20 15"><rect x="1" y="2" width="18" height="12" fill="none" stroke="#F7941D" stroke-width="1.8"/><path d="M1 2l9 7 9-7" fill="none" stroke="#F7941D" stroke-width="1.8"/></svg>Subsrcribe now to stay notified</h2>
    <div class="sub-form"><span class="sub-input">Your Email Address</span><span class="sub-btn">Subscribe</span></div>
  </section>
  <footer class="footer">
    <div class="social-dots" aria-label="Social links"><span></span><span></span><span></span><span></span><span></span></div>
    <p class="foot-links"><a href="#">Privacy Policy</a> | <a href="#">Specifications</a> | <a href="#">Sitemap</a></p>
  </footer>
</div>

<div class="screen mobile">
  <div class="topbar">
    <a class="phone" href="tel:+61755500148"><svg width="4" height="4" viewBox="0 0 24 24"><path fill="#fff" d="M6.6 10.8a15 15 0 0 0 6.6 6.6l2.2-2.2a1 1 0 0 1 1-.25 11.4 11.4 0 0 0 3.6.57 1 1 0 0 1 1 1V20a1 1 0 0 1-1 1A17 17 0 0 1 3 4a1 1 0 0 1 1-1h3.5a1 1 0 0 1 1 1c0 1.25.2 2.45.57 3.6a1 1 0 0 1-.25 1z"/></svg>61 7 5550 0148</a>
  </div>
  <header class="header">
    <a class="logo" href="#"><span class="logo-dot"></span><span class="logo-name">Harbourline<br>Plunge Tanks</span></a>
    <span class="burger" aria-label="Menu"><span></span><span></span><span></span></span>
  </header>
  <div class="step-head"><span>01 - Pool Size</span><a class="step-next" href="#">Next Option - Interval Colors &#8594;</a></div>
  <div class="gallery">
    <div class="photo-frame">
      <div class="tank-render" role="img" aria-label="Product render of a container plunge tank with dark cladding and blue interior"></div>
      <span class="arrow prev">&#8592;</span><span class="arrow next">&#8594;</span>
    </div>
    <div class="thumbs">
      <div class="thumb"><i role="img" aria-label="Tank view"></i></div>
      <div class="thumb active"><i role="img" aria-label="Tank view"></i></div>
      <div class="thumb"><i role="img" aria-label="Tank view"></i></div>
      <div class="thumb"><i role="img" aria-label="Tank view"></i></div>
      <div class="thumb"><i role="img" aria-label="Tank view"></i></div>
    </div>
  </div>
  <div class="details">
    <h1 class="product-title">Harbourline Plunge Tank</h1>
    <p class="pid">Product ID: 123 Text Filler</p>
    <div class="acc-open">
      <div class="acc-head"><span>Description</span><span class="chev">&#8963;</span></div>
      <p class="acc-text">Lorem Ipsum is simply dummy text of the printing and typesetting industry. Lorem Ipsum has been the industry's standard dummy text ever since the 1500s, when an unknown printer took a galley of type and scrambled it to</p>
    </div>
    <div class="acc-row"><div class="acc-head"><span>Features</span><span class="chev">&#8964;</span></div></div>
    <div class="acc-row"><div class="acc-head"><span>Specifications</span><span class="chev">&#8964;</span></div></div>
    <div class="acc-row"><div class="acc-head"><span>Text Filler</span><span class="chev">&#8964;</span></div></div>
    <div class="sizes">
      <label>Select a Pool Size:</label>
      <div class="size active"><b>6m</b><small>6m x 2.4m</small></div>
      <div class="size"><b>12m</b><small>12m x 2.4m</small></div>
    </div>
  </div>
  <section class="subscribe">
    <svg width="9" height="7" viewBox="0 0 20 15"><rect x="1" y="2" width="18" height="12" fill="none" stroke="#F7941D" stroke-width="2"/><path d="M1 2l9 7 9-7" fill="none" stroke="#F7941D" stroke-width="2"/></svg>
    <h2 class="sub-title">Subscribe now to<br>stay notified</h2>
    <div class="sub-form"><span class="sub-input">Your Email Address</span><span class="sub-btn">Subscribe</span></div>
  </section>
  <footer class="footer">
    <div class="social-dots" aria-label="Social links"><span></span><span></span><span></span><span></span><span></span></div>
    <p class="foot-links"><a href="#">Privacy Policy</a> | <a href="#">Specifications</a> | <a href="#">Sitemap</a></p>
  </footer>
</div>

</body>
</html>
```